Kids school furniture

I am looking for someone to work with and help me design a brochure / 30 page catolougue.

I have a design I like just need someone to help make it stand out from the crowd.

My website is Pebbletots.ae

Regards Derek

Target Market(s)

Schools and nurseries

Industry/Entity Type

Education

Font styles to use
Serif

Requirements
Must have
• Must have content page
• 1) intro
• 2) storage cabinet
• 3) tables and seating
• 4) creative
• 5) play time
• Ages = reception - years 1 and 2 - years 3 and 4 - years 5-6
Nice to have
• Needs to have classroom layouts for reception, years 1 and 2,
• years 3 and 4, years 5 and 6
Should not have
• Do not want the brochure to be to busy with lots of colours

```html
<!DOCTYPE html>
<html lang="en">
<head>
<meta charset="utf-8">
<title>Pebble Tots – Flyers</title>
<link href="https://fonts.googleapis.com/css2?family=Fredoka:wght@600&family=Comic+Neue:wght@700&family=Roboto+Condensed:ital,wght@0,700;1,700&display=swap" rel="stylesheet">
<style>
  :root{
    --bg:#e4e4e4;
    --page:#ffffff;
    --sky:#1ea6e2;
    --sky-dark:#1877c9;
    --sun:#fbf2b8;
    --sun-light:#fffbe6;
    --stripe:#c9eff6;
    --stripe-light:#e3f8fb;
    --purple:#7a3b9b;
    --red:#e8202a;
    --orange:#ef6a23;
    --green:#1a9a3c;
    --kids:#f4d9a8;
    --photo:#c9a56a;
    --ink-white:#ffffff;
  }
  *{margin:0;padding:0;box-sizing:border-box}
  html,body{width:1200px;height:645px;overflow:hidden;background:var(--bg)}
  .canvas{position:relative;width:1200px;height:645px}
  .flyer{position:absolute;top:18px;width:416px;height:582px;background:var(--page);overflow:hidden}
  .flyer--intro{left:90px}
  .flyer--storage{left:692px}
  .abs{position:absolute}
  .heading{font-family:"Fredoka",sans-serif;font-weight:600;text-align:center;width:100%;left:0;
    color:var(--sky);text-shadow:0 0 3px #fff,0 0 3px #fff,0 0 3px #fff}
  .sunburst{position:absolute;left:0;top:0;width:416px;height:290px}
  /* intro */
  .intro-title{top:14px;font-size:48px;line-height:1}
  .title-rule{left:93px;top:64px;width:230px;border-top:2px dotted var(--red)}
  .tagline{font-family:"Comic Neue",cursive;font-weight:700;text-align:center;width:100%;left:0}
  .tagline--one{top:72px;font-size:25px;color:var(--orange)}
  .tagline--one b{color:var(--purple)}
  .tagline--two{top:100px;font-size:32px;color:var(--green)}
  .brand{display:flex;align-items:center;justify-content:center;gap:10px;width:100%;left:0;
    font-family:"Fredoka",sans-serif;font-weight:600;color:var(--purple)}
  .brand__dot{width:26px;height:26px;border-radius:50%;background:var(--orange)}
  .intro-brand{top:170px;font-size:44px}
  .side-line{position:absolute;top:212px;bottom:0;width:2px}
  .side-line--red{background:var(--red)}
  .side-line--blue{background:var(--sky)}
  .mission{top:290px;left:0;width:100%;text-align:center;font-family:"Roboto Condensed",sans-serif;
    font-weight:700;font-size:13px;line-height:21px;color:var(--sky)}
  .mission strong{color:var(--red);font-size:17px}
  .kids-art{left:22px;top:338px;width:372px;height:94px;border-radius:10px;
    background:linear-gradient(90deg,#f7e3bd,#fdeedd 50%,#f7e3bd)}
  .contact-box{left:50px;top:438px;width:312px;height:72px;background:var(--purple);
    border:2px solid #f6d22b;border-radius:3px;color:var(--ink-white);
    font-family:"Roboto Condensed",sans-serif;font-weight:700;font-size:15px;line-height:21px;
    display:flex;flex-direction:column;align-items:center;justify-content:center}
  .contact-box svg{width:10px;height:10px;margin-right:4px;vertical-align:-1px}
  .social{left:84px;top:529px;display:flex;gap:9px}
  .social span{width:27px;height:27px;border-radius:4px;background:var(--sky-dark)}
  /* storage */
  .storage-title{top:20px;font-size:36px;line-height:40px}
  .storage-brand{top:108px;font-size:42px}
  .photo{position:absolute;background:#fff;padding:5px;box-shadow:1px 2px 5px rgba(0,0,0,.35)}
  .photo div{width:100%;height:100%}
  .photo--trolley{left:6px;top:252px;width:150px;height:120px;transform:rotate(5deg)}
  .photo--trolley div{background:linear-gradient(160deg,#f0e6d4,#f2c530 70%,#d9b25e)}
  .photo--shelf{left:146px;top:250px;width:132px;height:160px;transform:rotate(-1deg)}
  .photo--shelf div{background:linear-gradient(180deg,#e9e1cf,var(--photo) 60%,#b98d55)}
  .photo--lockers{left:270px;top:252px;width:140px;height:126px;transform:rotate(-6deg)}
  .photo--lockers div{background:linear-gradient(135deg,#d8323a,#2f7bc6 40%,#2da14f 70%,#f1c22e)}
  .label{position:absolute;font-family:"Roboto Condensed",sans-serif;font-weight:700;color:var(--purple);
    font-size:14px;line-height:17px;text-align:center;text-shadow:0 0 3px #fff,0 0 3px #fff}
  .price{display:block;color:var(--red);font-size:14px;margin-top:3px}
  .label--trolley{left:10px;top:380px;width:140px;transform:rotate(6deg)}
  .label--shelf{left:136px;top:436px;width:160px}
  .label--lockers{left:300px;top:395px;width:100px;transform:rotate(-10deg)}
  .footer{position:absolute;left:0;bottom:0;width:416px;height:76px;background:var(--purple);
    color:var(--ink-white);font-family:"Roboto Condensed",sans-serif;font-weight:700}
  .footer__scallop{position:absolute;left:0;top:-6px;width:416px;height:10px}
  .footer__lead{position:absolute;left:10px;top:18px;font-size:8.5px;line-height:13px;font-style:italic}
  .footer__lead b{font-size:11.5px}
  .footer__col{position:absolute;top:17px;font-size:10px;line-height:13px}
  .footer__col svg{width:8px;height:8px;margin-right:4px;vertical-align:-1px}
</style>
</head>
<body>
<div class="canvas">

  <section class="flyer flyer--intro">
    <svg class="sunburst" viewBox="0 0 416 290" aria-hidden="true">
      <defs>
        <radialGradient id="sunIntro" cx="50%" cy="70%" r="70%">
          <stop offset="0" stop-color="#fffde8"/><stop offset="1" stop-color="#fbf0ae"/>
        </radialGradient>
      </defs>
      <polygon points="0,0 416,0 416,210 208,262 0,210" fill="url(#sunIntro)"/>
      <polygon points="0,210 208,262 416,210 416,220 208,278 0,220" fill="var(--sky-dark)"/>
      <polygon points="0,220 208,278 416,220 416,224 208,283 0,224" fill="var(--sky)"/>
    </svg>
    <h1 class="abs heading intro-title">PEBBLE TOTS</h1>
    <div class="abs title-rule"></div>
    <p class="abs tagline tagline--one">HELPING MAKE <b>DREAMS</b></p>
    <p class="abs tagline tagline--two">COME TRUE!</p>
    <div class="abs brand intro-brand"><span class="brand__dot"></span>PEBBLE TOTS</div>

    <span class="side-line side-line--red" style="left:8px"></span>
    <span class="side-line side-line--blue" style="left:14px"></span>
    <span class="side-line side-line--red" style="left:386px"></span>
    <span class="side-line side-line--blue" style="left:394px"></span>

    <p class="abs mission">THROUGHOUT ALL OUR PROJECTS IT IS PEBBLE TOTS NUMBER<br>ONE GOAL TO ACHIEVE <strong>100%</strong> CLIENT SATISFACTION!</p>
    <div class="abs kids-art" role="img" aria-label="Illustration of six cartoon children holding hands"></div>

    <div class="abs contact-box">
      <p><svg viewBox="0 0 10 10"><path d="M2 1l2 2-1 1c.6 1.3 1.7 2.4 3 3l1-1 2 2-1.5 1.5C4 9 1 6 .5 2.5z" fill="#fff"/></svg>971 555 010 123 / <svg viewBox="0 0 10 10"><path d="M2 1l2 2-1 1c.6 1.3 1.7 2.4 3 3l1-1 2 2-1.5 1.5C4 9 1 6 .5 2.5z" fill="#fff"/></svg>971 554 010 456</p>
      <p><svg viewBox="0 0 10 10"><rect x="0" y="2" width="10" height="7" fill="#fff"/><path d="M0 2l5 4 5-4" stroke="#7a3b9b" fill="none"/></svg>CONTACT@PEBBLETOTS.AE</p>
      <p><svg viewBox="0 0 10 10"><circle cx="5" cy="5" r="4.3" fill="none" stroke="#fff" stroke-width="1.2"/><path d="M1 5h8M5 1v8" stroke="#fff"/></svg>WWW.PEBBLETOTS.AE</p>
    </div>

    <div class="abs social" aria-label="Social media links">
      <span></span><span></span><span></span><span></span><span></span><span></span><span></span>
    </div>
  </section>

  <section class="flyer flyer--storage">
    <svg class="sunburst" viewBox="0 0 416 582" style="height:582px" aria-hidden="true">
      <defs>
        <radialGradient id="sunStorage" cx="50%" cy="80%" r="70%">
          <stop offset="0" stop-color="#fffde8"/><stop offset="1" stop-color="#fbf0ae"/>
        </radialGradient>
        <linearGradient id="stripes" x1="0" x2="1">
          <stop offset="0" stop-color="#c6eef5"/><stop offset=".5" stop-color="#e3f8fb"/><stop offset="1" stop-color="#c6eef5"/>
        </linearGradient>
      </defs>
      <rect width="416" height="582" fill="url(#stripes)"/>
      <polygon points="0,0 416,0 416,136 208,198 0,136" fill="url(#sunStorage)"/>
      <polygon points="0,136 208,198 416,136 416,148 208,212 0,148" fill="var(--sky-dark)"/>
      <polygon points="0,148 208,212 416,148 416,152 208,217 0,152" fill="var(--sky)"/>
      <path d="M80 252L100 226 168 246M210 250L236 226 310 244M236 226L350 246" stroke="#6b6b6b" stroke-width="1" fill="none"/>
    </svg>
    <h1 class="abs heading storage-title">STORAGE<br>FURNITURE</h1>
    <div class="abs brand storage-brand"><span class="brand__dot"></span>PEBBLE TOTS</div>

    <figure class="photo photo--trolley"><div role="img" aria-label="Photo of a yellow classroom craft trolley with trays"></div></figure>
    <figure class="photo photo--shelf"><div role="img" aria-label="Photo of a wooden arts and crafts trolley holding books"></div></figure>
    <figure class="photo photo--lockers"><div role="img" aria-label="Photo of colourful numbered lockers"></div></figure>

    <p class="label label--trolley">CLASSROOM<br>CRAFT TROLLEY<span class="price">AED 2,500.00</span></p>
    <p class="label label--shelf">WOODEN ARTS AND<br>CRAFTS TROLLEY<span class="price">AED 1,500.00</span></p>
    <p class="label label--lockers">LOCKERS<span class="price">AED 1,600.00</span></p>

    <footer class="footer">
      <svg class="footer__scallop" viewBox="0 0 416 10" preserveAspectRatio="none" aria-hidden="true">
        <path d="M0 6 Q4 0 8 6 T16 6 T24 6 T32 6 T40 6 T48 6 T56 6 T64 6 T72 6 T80 6 T88 6 T96 6 T104 6 T112 6 T120 6 T128 6 T136 6 T144 6 T152 6 T160 6 T168 6 T176 6 T184 6 T192 6 T200 6 T208 6 T216 6 T224 6 T232 6 T240 6 T248 6 T256 6 T264 6 T272 6 T280 6 T288 6 T296 6 T304 6 T312 6 T320 6 T328 6 T336 6 T344 6 T352 6 T360 6 T368 6 T376 6 T384 6 T392 6 T400 6 T408 6 T416 6 V10 H0Z" fill="var(--red)"/>
      </svg>
      <p class="footer__lead">FOR MORE INFORMATION<br><b>PLEASE CONTACT</b></p>
      <p class="footer__col" style="left:138px">
        <svg viewBox="0 0 10 10"><path d="M2 1l2 2-1 1c.6 1.3 1.7 2.4 3 3l1-1 2 2-1.5 1.5C4 9 1 6 .5 2.5z" fill="#fff"/></svg>971 555 010 123<br>
        <svg viewBox="0 0 10 10"><path d="M2 1l2 2-1 1c.6 1.3 1.7 2.4 3 3l1-1 2 2-1.5 1.5C4 9 1 6 .5 2.5z" fill="#fff"/></svg>971 554 010 456
      </p>
      <p class="footer__col" style="left:252px">
        <svg viewBox="0 0 10 10"><rect x="0" y="2" width="10" height="7" fill="#fff"/><path d="M0 2l5 4 5-4" stroke="#7a3b9b" fill="none"/></svg>CONTACT@PEBBLETOTS.AE<br>
        <svg viewBox="0 0 10 10"><circle cx="5" cy="5" r="4.3" fill="none" stroke="#fff" stroke-width="1.2"/><path d="M1 5h8M5 1v8" stroke="#fff"/></svg>WWW.PEBBLETOTS.AE
      </p>
    </footer>
  </section>

</div>
</body>
</html>
```